・Webサイト作成サービス『ミモザ・サイトキット』内で、利用者が選択できるデザインテーマの新規作成依頼です。
・既存デザインとは異なる雰囲気のデザイン作成をお願いします。
・トップページのデザイン採用後、同テイストで一部下層ページのデザイン作成も依頼予定です

既存デザイン(サンプルサイトです)
https://sample.velorn.jp/

■サービス概要
・保険代理店向けのサブスクサービスです
・ノーコードでWebサイトを作成できます
・専用の管理画面から情報の追加や更新を行います
・Webサイトのデザインテーマも管理画面から選択します

サービスサイト
https://lp.velorn.jp/
・優しさを感じる「アットホーム」なデザインを希望します
・要素の角に丸みを持ったデザインとしてください
・色はブルー系で同系色にまとめてください
※ サービス移植後は基本色を変更し、12色での展開を予定しているため
・写真やバナー等の画像は既存サイトより保存して組み込んでください
※ 画像等はサービス共通のため、デザインいただく必要ありません
・表示内容は既存サイトを参考としてください
・CSSを変更するだけで対応可能な程度であれば多少のレイアウト変更はOKです
※ HTMLはそのままで、CSSを切り替えるだけでデザインを変える仕組みのため

■納品形式
Adobe XD での納品をお願いします。
https://sample.velorn.jp/
1ページ
青系
■納品形式
Adobe XD での納品をお願いします。
ページに表示するコンテンツの構成は変更できませんが、CSSで変更できる範囲で既存デザインとの違いを出したり、見た目の工夫をお願いします。

例えば...
・CSSの疑似要素を活用して見出しにあしらいを付ける
・背景へパターンを適用する
・お問い合わせボタンを絶対値で指定する
・既存のあしらい要素を非表示にする

さらに詳しく添付の画像に記載しておりますので、ご参照ください。
ご質問等あればお気軽にお願いします。

当該ランサーさんの初期の提案が、こちらの望んでいた雰囲気に一番近く、細かい部分にも丁寧な仕事ぶりが見られたことから、お声がけさせていただきました。
手直しの際もこちらの意図をしっかりと汲み取っていただき、少ない回数で望んだデザインへと至ることができました。

たくさんのご提案ありがとうございました。
また機会がございましたら、よろしくお願いいたします。

```html
<!DOCTYPE html>
<html lang="ja">
<head>
<meta charset="UTF-8">
<title>サンプル保険サービス</title>
<link href="https://fonts.googleapis.com/css2?family=Noto+Sans+JP:wght@400;500;700&family=Roboto:wght@400;500;700&display=swap" rel="stylesheet">
<style>
:root{
  --blue:#3d9fd1;
  --blue-dark:#2a7fb4;
  --blue-soft:#e6f2f8;
  --blue-pale:#f2f8fb;
  --sky:#cfe6f2;
  --text:#333c44;
  --muted:#7a8791;
  --line:#d9e3e9;
  --white:#ffffff;
  --gray-box:#d6d9dc;
  --footer-bg:#f4f7f9;
}
*{margin:0;padding:0;box-sizing:border-box}
html,body{width:1200px;height:3856px;overflow:hidden}
body{position:relative;font-family:"Noto Sans JP",sans-serif;color:var(--text);background:var(--white)}
.abs{position:absolute}
a{color:inherit;text-decoration:none}

/* header */
.site-header{left:0;top:0;width:1200px;height:120px;background:linear-gradient(180deg,#fff,#f5fafc)}
.logo{left:160px;top:36px;font-size:26px;font-weight:700;letter-spacing:.04em;color:var(--text)}
.header-tel{left:820px;top:26px;display:flex;align-items:center;gap:10px;color:var(--blue);font-family:"Roboto",sans-serif;font-weight:700;font-size:36px}
.header-hours{left:876px;top:72px;font-size:13px;color:var(--muted)}
.side-contact{left:1132px;top:0;width:68px;height:190px;background:var(--blue);border-radius:0 0 0 16px;color:#fff;writing-mode:vertical-rl;font-size:16px;font-weight:500;letter-spacing:.12em;display:flex;align-items:center;justify-content:center;white-space:nowrap}
.global-nav{left:160px;top:118px;width:940px;height:40px;display:flex;justify-content:space-around;align-items:center;font-size:15px;font-weight:500}

/* hero */
.hero-photo{left:160px;top:168px;width:1040px;height:544px;border-radius:40px 0 0 40px;background:linear-gradient(110deg,#e9f3e0 0%,#cfe3ec 35%,#8ea6b8 62%,#f0f2f1 100%)}
.hero-copy{left:72px;top:500px;font-size:36px;font-weight:700;line-height:1.7;letter-spacing:.06em;color:var(--text);text-shadow:0 0 12px #fff,0 0 4px #fff}

/* news bar */
.news-bar{left:160px;top:752px;width:880px;height:52px;background:#fff;border-radius:26px;box-shadow:0 4px 16px rgba(40,110,150,.12);display:flex;align-items:center;padding:0 30px;font-size:14px;gap:22px}
.news-bar .date{font-family:"Roboto",sans-serif;color:var(--muted)}
.tag{display:inline-block;width:88px;height:22px;border:1px solid var(--blue);border-radius:11px;color:var(--blue);font-size:11px;text-align:center;line-height:20px;flex-shrink:0}
.news-bar .ctrl{margin-left:auto;display:flex;gap:26px}
.dot-btn{width:26px;height:26px;border-radius:50%;background:var(--blue-soft);display:flex;align-items:center;justify-content:center}

/* intro cards */
.intro-bg{left:0;top:700px;width:1200px;height:1060px;background:linear-gradient(180deg,#fff 0%,var(--blue-pale) 40%,var(--blue-soft) 100%)}
.intro-card{left:260px;width:680px;height:248px;background:#fff;border-radius:24px;box-shadow:0 6px 20px rgba(40,110,150,.1);overflow:hidden;display:flex}
.intro-card .txt{width:340px;padding:44px 40px}
.intro-card h2{font-size:22px;color:var(--blue);font-weight:700;margin-bottom:20px;padding-left:18px;position:relative}
.intro-card h2::before{content:"";position:absolute;left:0;top:6px;width:8px;height:18px;border-radius:4px;background:var(--blue)}
.intro-card p{font-size:14px;line-height:2;color:var(--muted)}
.intro-card .img{width:340px;height:100%}
.card-about{top:872px}
.card-about .img{background:linear-gradient(135deg,#e9f4d4,#7fb86a 55%,#c9e2a8)}
.card-service{top:1160px}
.card-service .img{background:linear-gradient(135deg,#f6f0d8,#e8d98c 50%,#dbe4ea)}
.card-staff{top:1448px}
.card-staff .img{background:linear-gradient(135deg,#9fcbe0,#3f5e78 60%,#b9d6e4)}

/* section heading */
.sec-title{left:0;width:1200px;text-align:center}
.sec-title h2{font-size:30px;font-weight:700;letter-spacing:.08em}
.sec-title span{display:block;margin-top:8px;font-family:"Roboto",sans-serif;font-size:14px;color:var(--blue);letter-spacing:.15em}

/* online service */
.online{left:0;top:1760px;width:1200px;height:520px;background:var(--blue-soft)}
.svc-btn{width:264px;height:108px;background:#fff;border:3px solid var(--blue);border-radius:18px;display:flex;align-items:center;justify-content:center;gap:20px;color:var(--blue);font-weight:700;font-size:21px;line-height:1.3}

/* news */
.news-list{left:192px;top:2424px;width:828px}
.news-item{display:flex;align-items:center;gap:30px;height:70px;border-bottom:1px solid var(--line);font-size:14px}
.news-item .date{font-family:"Roboto",sans-serif;color:var(--muted);width:90px}
.btn-more{left:472px;top:2716px;width:256px;height:52px;border-radius:26px;background:var(--blue);color:#fff;font-size:15px;font-weight:500;display:flex;align-items:center;justify-content:center;box-shadow:0 4px 10px rgba(40,110,150,.2)}

/* links */
.links{left:0;top:2840px;width:1200px;height:220px;background:var(--footer-bg)}
.link-box{top:2966px;width:200px;height:64px;border:2px solid var(--line);background:#fff;border-radius:12px;color:#b5bcc2;font-size:16px;display:flex;align-items:center;justify-content:center}

/* contact band */
.contact-band{left:0;top:3060px;width:1200px;height:170px;background:linear-gradient(90deg,#2f8ec4,#5fb6e0)}
.band-tel{left:256px;top:3096px;color:#fff;font-family:"Roboto",sans-serif;font-weight:700;font-size:40px;display:flex;align-items:center;gap:12px}
.band-hours{left:310px;top:3152px;color:#e4f3fb;font-size:13px}
.band-btn{left:600px;top:3098px;width:340px;height:64px;border:2px solid #fff;border-radius:32px;color:#fff;font-weight:700;font-size:20px;display:flex;align-items:center;justify-content:center;gap:12px}

/* footer */
.footer-nav{left:300px;top:3254px;width:600px;display:flex;justify-content:space-between;font-size:14px}
.footer-info{left:160px;top:3310px;width:880px;height:260px;border-top:1px solid var(--line);padding-top:28px;display:flex;gap:40px}
.company{width:320px;font-size:12px;line-height:1.9;color:var(--muted)}
.company .label{color:var(--blue);font-weight:500}
.company .name{font-size:16px;font-weight:700;color:var(--text)}
.notes{flex:1;font-size:11px;line-height:1.9;color:var(--muted)}
.notes p{margin-bottom:6px}
.ft-banner{top:3620px;width:176px;height:80px;background:var(--gray-box);border-radius:12px;color:#fff;font-size:16px;display:flex;align-items:center;justify-content:center}
.bottom-bar{left:0;top:3764px;width:1200px;height:92px;border-top:1px solid var(--line)}
.bottom-links{left:160px;top:3780px;display:flex;gap:24px;font-size:11px;color:var(--muted)}
.share{top:3778px;width:66px;height:20px;border-radius:4px}
.copyright{left:0;top:3824px;width:1200px;text-align:center;font-size:11px;color:var(--muted)}
</style>
</head>
<body>

<header class="site-header abs"></header>
<div class="logo abs">サンプル保険サービス</div>
<div class="header-tel abs">
  <svg width="30" height="30" viewBox="0 0 30 30"><circle cx="15" cy="15" r="15" fill="#3d9fd1"/><path d="M10 8c1 0 2 2 2.5 3.2.3.8-1 1.6-.9 2.3.4 1.6 2.3 3.5 3.9 3.9.7.1 1.5-1.2 2.3-.9C19 17 21 18 21 19c0 1.2-1.5 3-3 3-5 0-10-5-10-10 0-1.5 1-4 2-4z" fill="#fff"/></svg>
  123-456-7890
</div>
<div class="header-hours abs">営業時間 9:00-17:00（土日祝・休業日）</div>
<a class="side-contact abs" href="#">お問い合わせ</a>
<nav class="global-nav abs">
  <a href="#">ホーム</a><a href="#">当社について</a><a href="#">サービスのご案内</a><a href="#">スタッフ紹介</a><a href="#">お知らせ</a>
</nav>

<div class="intro-bg abs"></div>
<div class="hero-photo abs" role="img" aria-label="スーツ姿のスタッフ3名が並ぶ写真"></div>
<p class="hero-copy abs">お客さま一人ひとりに合った<br>保険を提案します</p>

<div class="news-bar abs">
  <span class="date">2021.04.16</span><span class="tag">お知らせ</span>
  <span>コロナ禍における対応の取り組み</span>
  <span class="ctrl">
    <span class="dot-btn"><svg width="10" height="10" viewBox="0 0 10 10"><path d="M3 1l4 4-4 4" stroke="#3d9fd1" stroke-width="2" fill="none"/></svg></span>
    <span class="dot-btn"><svg width="12" height="10" viewBox="0 0 12 10"><path d="M0 1h12M0 5h12M0 9h12" stroke="#3d9fd1" stroke-width="2"/></svg></span>
  </span>
</div>

<section class="intro-card card-about abs">
  <div class="txt"><h2>当社について</h2><p>会社情報、アクセスなど、当社についての概要をご覧いただけます。</p></div>
  <div class="img" role="img" aria-label="木漏れ日が差す木々の写真"></div>
</section>
<section class="intro-card card-service abs">
  <div class="img" role="img" aria-label="書類とペンが置かれた机の写真"></div>
  <div class="txt"><h2>サービスのご案内</h2><p>お客さまの状況や目的に合わせて選べる、様々な保険商品をご用意しております。</p></div>
</section>
<section class="intro-card card-staff abs">
  <div class="txt"><h2>スタッフ紹介</h2><p>保険のプロフェッショナルが丁寧にサポートします。お気軽にご相談ください。</p></div>
  <div class="img" role="img" aria-label="スーツ姿のスタッフの写真"></div>
</section>

<section class="online abs"></section>
<div class="sec-title abs" style="top:1822px"><h2>オンラインサービス</h2><span>- ONLINE SERVICE -</span></div>
<a class="svc-btn abs" style="left:168px;top:1932px" href="#">
  <svg width="44" height="40" viewBox="0 0 44 40"><path d="M22 38S2 26 2 13C2 6 7 2 12 2c4 0 8 3 10 6 2-3 6-6 10-6 5 0 10 4 10 11 0 13-20 25-20 25z" fill="#3d9fd1"/></svg>
  <span>サンプル<br>生命保険</span></a>
<a class="svc-btn abs" style="left:468px;top:1932px" href="#">
  <svg width="48" height="40" viewBox="0 0 48 40"><path d="M8 18l5-10h22l5 10h4v12h-4v4h-6v-4H14v4H8v-4H4V18z" fill="#3d9fd1"/><circle cx="13" cy="24" r="3" fill="#fff"/><circle cx="35" cy="24" r="3" fill="#fff"/></svg>
  <span>サンプル<br>自転車保険</span></a>
<a class="svc-btn abs" style="left:768px;top:1932px" href="#">
  <svg width="48" height="40" viewBox="0 0 48 40"><path d="M6 20l6-12h24l6 12h2v12h-4v4h-6v-4H14v4H8v-4H4V20z" fill="#3d9fd1"/><rect x="14" y="11" width="20" height="8" rx="2" fill="#fff"/></svg>
  <span>サンプル<br>自動車保険</span></a>
<a class="svc-btn abs" style="left:168px;top:2064px" href="#">
  <svg width="44" height="44" viewBox="0 0 44 44"><path d="M40 4c-2-2-6 0-9 3l-6 6L8 8l-4 4 13 8-6 6-5-1-3 3 7 4 4 7 3-3-1-5 6-6 8 13 4-4-5-17 6-6c3-3 5-7 3-9z" fill="#3d9fd1"/></svg>
  <span>サンプル<br>旅行保険</span></a>
<a class="svc-btn abs" style="left:468px;top:2064px" href="#">
  <svg width="40" height="44" viewBox="0 0 40 44"><circle cx="20" cy="18" r="16" fill="#3d9fd1"/><rect x="16" y="32" width="8" height="10" rx="2" fill="#3d9fd1"/></svg>
  <span>サンプル<br>ゴルフ保険</span></a>

<div class="sec-title abs" style="top:2320px"><h2>新着情報</h2><span>- NEWS -</span></div>
<div class="news-list abs">
  <div class="news-item"><span class="date">2021.04.16</span><span class="tag">お知らせ</span><span>コロナ禍における対応の取り組み</span></div>
  <div class="news-item"><span class="date">2020.09.23</span><span class="tag">保険の知識</span><span>台風への備えチェックポイント</span></div>
  <div class="news-item"><span class="date">2020.09.10</span><span class="tag">お知らせ</span><span>マネープラン面談のオンラインサービスご案内</span></div>
  <div class="news-item"><span class="date">2021.04.16</span><span class="tag">お知らせ</span><span>新型コロナウイルス対応状況について</span></div>
</div>
<a class="btn-more abs" href="#">一覧を見る</a>

<section class="links abs"></section>
<div class="sec-title abs" style="top:2870px"><h2>関連リンク</h2><span>- LINK -</span></div>
<a class="link-box abs" style="left:160px" href="#">サンプル損保</a>
<a class="link-box abs" style="left:420px" href="#">サンプル生命</a>
<a class="link-box abs" style="left:680px" href="#">SAMPLE生命</a>
<a class="link-box abs" style="left:940px" href="#">公式フォトアカウント</a>

<section class="contact-band abs"></section>
<div class="band-tel abs">
  <svg width="36" height="36" viewBox="0 0 30 30"><circle cx="15" cy="15" r="15" fill="#fff"/><path d="M10 8c1 0 2 2 2.5 3.2.3.8-1 1.6-.9 2.3.4 1.6 2.3 3.5 3.9 3.9.7.1 1.5-1.2 2.3-.9C19 17 21 18 21 19c0 1.2-1.5 3-3 3-5 0-10-5-10-10 0-1.5 1-4 2-4z" fill="#3d9fd1"/></svg>
  123-456-7890
</div>
<div class="band-hours abs">営業時間 9:00-17:00（土日祝・休業日）</div>
<a class="band-btn abs" href="#">
  <svg width="22" height="16" viewBox="0 0 22 16"><rect x="1" y="1" width="20" height="14" rx="2" fill="none" stroke="#fff" stroke-width="2"/><path d="M1 2l10 7 10-7" fill="none" stroke="#fff" stroke-width="2"/></svg>
  お問い合わせ</a>

<nav class="footer-nav abs">
  <a href="#">ホーム</a><a href="#">当社について</a><a href="#">サービスのご案内</a><a href="#">スタッフ紹介</a><a href="#">お知らせ</a>
</nav>
<footer class="footer-info abs">
  <div class="company">
    <p class="label">■ 取扱代理店</p>
    <p class="name">サンプル保険サービス株式会社</p>
    <p>〒000-0000</p>
    <p>東京都中央区サンプル町1-2-3 サンプルビル5F</p>
    <p>TEL 123-456-7890 / FAX 123-456-7891</p>
  </div>
  <div class="notes">
    <p>● 当社は複数の保険会社の代理店として契約の締結を代理しております。</p>
    <p>● 保険商品の詳細はパンフレットや重要事項説明書をよくお読みのうえ、ご不明点は担当者までお問い合わせください。</p>
    <p>● 本サイトに記載の内容は概要を説明したものです。補償内容や条件は商品ごとに異なりますので、ご契約前に必ずご確認ください。</p>
    <p>● お客さまの個人情報は適切に管理し、保険のご案内およびサービス向上の目的にのみ利用いたします。</p>
  </div>
</footer>
<div class="ft-banner abs" style="left:160px">バナー</div>
<div class="ft-banner abs" style="left:400px">バナー</div>
<div class="ft-banner abs" style="left:640px">バナー</div>
<div class="ft-banner abs" style="left:880px">バナー</div>

<div class="bottom-bar abs"></div>
<div class="bottom-links abs">
  <a href="#">勧誘方針</a><a href="#">個人情報保護方針</a><a href="#">反社会的勢力への対応</a><a href="#">サイトマップ</a>
</div>
<span class="share abs" style="left:810px;background:#3d9fd1"></span>
<span class="share abs" style="left:886px;background:#5fb6e0"></span>
<span class="share abs" style="left:962px;background:#2a7fb4"></span>
<p class="copyright abs">© 2021 サンプル保険サービス All Rights Reserved.</p>

</body>
</html>
```